Marrowind Booking Engine Marketing Site

Hi,
I’m currently in the process of putting together a web application with the intention of providing small resorts/B&Bs/small hotels the ability to allow their customers to book online.
I’m looking to have a design created for a marketing site, to give potential customers additional information about my booking engine, as well as to help drive sign-ups. A lot of the competition out there appears outdated, so I would like something that is more modern and up to date.
I am looking for just the design (i’m a web developer, but I lack the creative skills for a good marketing site)
For some more background, I will be targeting business owners of smaller resorts and Bed & Breakfasts. These are typically family owned small businesses that may only have a 10 room setup. These businesses will also typically have additional amenities that they will have to rent out or sell to their clients ( ex. Spa, fruit basket, water sport rentals). My software will provide them with the ability to sell their amenities as well.
I’m open to different designs, but my main thing is I want it to look modern, and I want it to have several callouts to sign up for my product.
I am looking to have the homepage created, 1 interior page, and a style guide created (to show form fields, H1’s, etc.).
I had a logo created a couple months ago that will be included with this project brief.
If you need any additional information feel free to reach out to me.

Target Market(s)

This site will be targeted small business owners who are running small resorts, Bed and Breakfasts, or any business that provides rooms for their clients.

Industry/Entity Type

Saas

Number of Pages Required

2 page

Font styles to use
Sans Serif

Colors

Designer to choose colors to be used in the design.

Requirements
Must have
• A modern feel, with several CTA's that will drive to the registration page on the homepage. on the internal page, I mostly just need the page layout, I will reuse that page layout. and a style guide if at all possible (include colors, form fields, H1's, etc.)
Nice to have
• maybe a hero image at the top with buttons over the top? again i'm pretty open to most anything.
Should not have
• I like images, but I don't want the page overrun with images. A good balance.

```html
<!DOCTYPE html>
<html lang="en">
<head>
<meta charset="utf-8">
<title>Marrowind Booking Engine</title>
<link href="https://fonts.googleapis.com/css2?family=Roboto:wght@300;400;500;700&display=swap" rel="stylesheet">
<style>
:root{
  --cyan:#45d0ec;
  --cyan-deep:#2fb9dc;
  --blue:#4aa7e0;
  --green:#69bd1c;
  --teal-dark:#2c6878;
  --ink:#222a30;
  --muted:#8a939a;
  --line:#d9dee2;
  --paper:#ffffff;
  --mist:#f1f4f6;
  --bar:#eceff1;
}
*{box-sizing:border-box;margin:0;padding:0}
html,body{width:1200px;height:4242px;overflow:hidden}
body{position:relative;font-family:'Roboto',Arial,sans-serif;color:var(--ink);background:var(--paper)}
.abs{position:absolute}
.btn{position:absolute;height:30px;border-radius:15px;font-size:13px;font-weight:500;letter-spacing:.5px;text-transform:uppercase;display:flex;align-items:center;justify-content:center;color:#fff}
.btn-green{background:var(--green)}
.btn-ghost{border:2px solid #fff}

/* header & hero */
.hero{left:0;top:0;width:1200px;height:560px;background:linear-gradient(160deg,#56dbf2 0%,var(--cyan) 45%,var(--cyan-deep) 100%);overflow:hidden}
.brand{display:flex;align-items:center;gap:10px;font-size:22px;font-weight:500}
.brand-dot{width:22px;height:22px;border-radius:50%;background:var(--green)}
.hero .brand{left:133px;top:32px;color:#fff}
.nav{left:400px;top:40px;display:flex;gap:44px;font-size:13px;font-weight:500;color:#fff;text-transform:uppercase}
.nav .active{border-bottom:2px solid #fff;padding-bottom:6px}
.hero h1{left:133px;top:205px;width:560px;font-size:38px;line-height:48px;font-weight:700;color:#fff}
.hero-photo{left:665px;top:150px;width:440px;height:390px;border-radius:30px 30px 0 0;background:linear-gradient(160deg,#f4f6f8,#c9d3da)}

h2.sec{font-size:26px;line-height:40px;font-weight:500;color:var(--ink)}
p.body{font-size:15px;line-height:25px;color:var(--muted)}
.tablet{border-radius:16px;background:linear-gradient(180deg,#f7f8f9,#e3e7ea);box-shadow:0 10px 24px rgba(0,0,0,.18)}

/* key features */
.features{left:0;top:1415px;width:1200px;height:610px;background:linear-gradient(135deg,#3e8597 0%,var(--teal-dark) 55%,#255c6c 100%);overflow:hidden}
.features h2{position:absolute;left:0;width:1200px;top:95px;text-align:center;color:#fff;font-size:28px;font-weight:500}
.features h2::after{content:"";display:block;width:60px;height:2px;background:#fff;margin:10px auto 0}
.feat{position:absolute;width:300px;text-align:center;color:#fff;font-size:19px;font-weight:400}
.feat svg{display:block;margin:0 auto 10px}

/* additional */
.additional{left:0;top:2025px;width:1200px;height:655px;background:var(--mist)}
.card{position:absolute;width:459px;height:170px;background:#fff;box-shadow:0 3px 12px rgba(0,0,0,.05)}
.card svg{position:absolute;left:38px;top:38px}
.card h3{position:absolute;left:135px;top:36px;font-size:19px;font-weight:500}
.card p{position:absolute;left:135px;top:68px;width:290px;font-size:14px;line-height:22px;color:var(--muted)}

/* cta */
.cta{left:0;top:2680px;width:1200px;height:470px;background:linear-gradient(150deg,#55b3ea 0%,var(--blue) 50%,#3b9ad8 100%);overflow:hidden}
.cta-photo{left:0;top:60px;width:400px;height:300px;border-radius:0 150px 150px 0;background:linear-gradient(90deg,#f3e6dc,#e2cfc1)}
.cta h2{left:453px;top:175px;width:520px;font-size:30px;line-height:40px;font-weight:700;color:#fff}
.cta p{left:453px;top:275px;width:540px;font-size:15px;line-height:25px;color:#fff}

/* news */
.news-title{right:133px;top:3205px;font-size:30px;font-weight:500}
.news-sub{right:133px;top:3262px;font-size:15px;color:var(--muted)}
.news{position:absolute;top:3345px;width:459px;height:390px;background:#fff;box-shadow:0 3px 14px rgba(0,0,0,.08)}
.news .thumb{height:210px}
.news .date{position:absolute;left:0;top:0;width:70px;height:70px;background:var(--cyan);border-radius:0 0 70px 0;color:#fff;padding:10px 0 0 14px;font-size:22px;line-height:22px}
.news .date small{display:block;font-size:10px;letter-spacing:1px}
.news h3{position:absolute;left:22px;top:232px;font-size:20px;font-weight:500}
.news p{position:absolute;left:22px;top:268px;width:420px;font-size:14px;line-height:21px;color:var(--muted)}
.news a{position:absolute;left:22px;top:342px;font-size:13px;color:var(--cyan-deep);text-decoration:none;text-transform:uppercase}

/* footer */
.footer{left:0;top:3843px;width:1200px;height:317px;background:#fff;border-top:1px solid #eef0f2}
.footer .brand{position:absolute;left:133px;top:62px;color:var(--ink)}
.footer .about{position:absolute;left:133px;top:120px;width:270px;font-size:13px;line-height:20px;color:var(--muted)}
.socials{position:absolute;left:133px;top:202px;display:flex;gap:14px}
.socials span{width:12px;height:12px;border-radius:50%;background:#9aa3aa}
.contact{position:absolute;left:453px;font-size:13px;line-height:19px;color:var(--muted);display:flex;gap:16px}
.field{position:absolute;height:32px;border:1px solid var(--line);font-size:12px;color:#9aa3aa;padding:8px 14px}
.bottom-bar{left:0;top:4160px;width:1200px;height:82px;background:var(--bar);font-size:13px;color:#6b747b}
.bottom-bar .copy{position:absolute;left:133px;top:33px}
.bottom-bar nav{position:absolute;right:133px;top:33px;display:flex;gap:40px;text-transform:uppercase}
</style>
</head>
<body>

<header class="abs hero">
  <svg class="abs" style="left:0;top:0" width="1200" height="560" aria-hidden="true">
    <polygon points="520,0 1200,0 1200,300 760,560 600,560" fill="#fff" opacity=".07"/>
    <polygon points="0,330 420,560 0,560" fill="#fff" opacity=".06"/>
    <path d="M0,470 C300,560 620,560 900,520 C1030,500 1120,470 1200,440 L1200,560 L0,560 Z" fill="#fff"/>
  </svg>
  <div class="abs brand"><span class="brand-dot"></span>Marrowind</div>
  <nav class="abs nav">
    <span class="active">Home</span><span>How it works</span><span>About</span><span>Interior</span><span>Contact us</span>
  </nav>
  <div class="btn btn-green" style="left:935px;top:33px;width:130px">Sign up</div>
  <h1 class="abs">We Help Your Business Attract More Customers</h1>
  <div class="btn btn-green" style="left:133px;top:330px;width:176px">Sign up</div>
  <div class="btn btn-ghost" style="left:332px;top:330px;width:176px">Learn more</div>
  <div class="abs hero-photo" role="img" aria-label="Hand holding a smartphone showing a list of resort rooms"></div>
</header>

<section>
  <div class="abs tablet" style="left:133px;top:665px;width:382px;height:270px" role="img" aria-label="Tablet showing the room selection screen of the booking engine"></div>
  <h2 class="abs sec" style="left:575px;top:688px;width:500px">An Ideal Solution for Business Owners of Smaller Resorts</h2>
  <p class="abs body" style="left:575px;top:780px;width:492px">Sed ut perspiciatis unde omnis iste natus error sit voluptatem accusantium doloremque laudantium, totam rem aperiam, eaque ipsa quae ab illo inventore veritatis et quasi architecto beatae vitae dicta sunt explicabo. Nemo enim ipsam voluptatem quia voluptas sit aspernatur aut odit aut fugit,</p>

  <h2 class="abs sec" style="left:133px;top:1065px;width:470px">A Simple Interface - Your Customers Will Never be Frustrated</h2>
  <p class="abs body" style="left:133px;top:1155px;width:492px">Sed ut perspiciatis unde omnis iste natus error sit voluptatem accusantium doloremque laudantium, totam rem aperiam, eaque ipsa quae ab illo inventore veritatis et quasi architecto beatae vitae dicta sunt explicabo. Nemo enim ipsam voluptatem quia voluptas sit aspernatur aut odit aut fugit,</p>
  <div class="abs tablet" style="left:680px;top:1047px;width:382px;height:270px" role="img" aria-label="Tablet showing the booking calendar dashboard"></div>
</section>

<section class="abs features" role="img" aria-label="Person holding a phone, tinted teal, behind the key features">
  <svg class="abs" style="left:0;top:0" width="1200" height="610" aria-hidden="true">
    <path d="M0,575 C350,540 800,520 1200,455 L1200,610 L0,610 Z" fill="var(--mist)"/>
  </svg>
  <h2>Key Features</h2>
  <div class="feat" style="left:132px;top:180px"><svg width="48" height="48" fill="none" stroke="#8fd14f" stroke-width="2"><circle cx="24" cy="18" r="9"/><path d="M10 44 C14 32 34 32 38 44"/></svg>Booking Management</div>
  <div class="feat" style="left:450px;top:180px"><svg width="48" height="48" fill="none" stroke="#ff6b5b" stroke-width="2"><rect x="10" y="14" width="28" height="28"/><path d="M16 14 V8 H32 V14"/></svg>Amenity Management</div>
  <div class="feat" style="left:765px;top:180px"><svg width="48" height="48" fill="none" stroke="#f4c430" stroke-width="2"><path d="M8 26 L24 12 L40 26"/><path d="M14 22 V40 H34 V22"/></svg>Property Management</div>
  <div class="feat" style="left:132px;top:330px"><svg width="48" height="48" fill="none" stroke="#f39c2b" stroke-width="2"><rect x="8" y="10" width="32" height="22"/><path d="M18 40 H30 M24 32 V40"/></svg>Online Booking</div>
  <div class="feat" style="left:450px;top:330px"><svg width="48" height="48" fill="none" stroke="#c06bd6" stroke-width="2"><path d="M12 6 H36 V42 H12 Z"/><path d="M18 16 H30 M18 24 H30 M18 32 H26"/></svg>Invoicing</div>
  <div class="feat" style="left:765px;top:330px"><svg width="48" height="48" fill="none" stroke="#4fc3e8" stroke-width="2"><path d="M8 20 H20 L36 10 V38 L20 28 H8 Z"/></svg>Promotions capabilities</div>
  <div class="btn btn-green" style="left:515px;top:488px;width:176px">Sign up</div>
</section>

<section class="abs additional">
  <h2 class="abs sec" style="left:133px;top:52px;font-size:28px">Additional Features</h2>
  <div class="abs" style="left:133px;top:94px;width:40px;height:2px;background:var(--ink)"></div>
  <p class="abs body" style="left:133px;top:108px">Lorem ipsum dolor sit amet, consectetur adipiscing elit</p>

  <div class="card" style="left:133px;top:188px"><svg width="62" height="62" fill="none" stroke="var(--cyan)" stroke-width="2"><circle cx="31" cy="31" r="10"/><circle cx="31" cy="8" r="5"/><circle cx="8" cy="40" r="5"/><circle cx="54" cy="40" r="5"/></svg><h3>Multi-User capabilities</h3><p>Lorem ipsum dolor sit amet, consectetur adipiscing elit, sed do eiusmod tempor incididunt ut labore</p></div>
  <div class="card" style="left:608px;top:188px"><svg width="62" height="62" fill="none" stroke="var(--cyan)" stroke-width="2"><circle cx="31" cy="31" r="10"/><circle cx="31" cy="8" r="5"/><circle cx="8" cy="40" r="5"/><circle cx="54" cy="40" r="5"/></svg><h3>Multi-Property capabilities</h3><p>Lorem ipsum dolor sit amet, consectetur adipiscing elit, sed do eiusmod tempor incididunt ut labore</p></div>
  <div class="card" style="left:133px;top:378px"><svg width="62" height="62" fill="none" stroke="var(--cyan)" stroke-width="2"><circle cx="31" cy="31" r="10"/><circle cx="31" cy="8" r="5"/><circle cx="8" cy="40" r="5"/><circle cx="54" cy="40" r="5"/></svg><h3>Rates Management</h3><p>Lorem ipsum dolor sit amet, consectetur adipiscing elit, sed do eiusmod tempor incididunt ut labore</p></div>
  <div class="card" style="left:608px;top:378px"><svg width="62" height="62" fill="none" stroke="var(--cyan)" stroke-width="2"><circle cx="31" cy="31" r="10"/><circle cx="31" cy="8" r="5"/><circle cx="8" cy="40" r="5"/><circle cx="54" cy="40" r="5"/></svg><h3>Integrated Analytics Tracking</h3><p>Lorem ipsum dolor sit amet, consectetur adipiscing elit, sed do eiusmod tempor incididunt ut labore</p></div>
</section>

<section class="abs cta">
  <svg class="abs" style="left:0;top:0" width="1200" height="470" aria-hidden="true">
    <polygon points="600,0 1200,0 1200,260" fill="#fff" opacity=".07"/>
    <path d="M0,400 C300,450 700,440 1200,360 L1200,470 L0,470 Z" fill="#fff"/>
  </svg>
  <div class="abs cta-photo" role="img" aria-label="Hand holding a house key on a keyring"></div>
  <h2 class="abs">Lorem Ipsum Dolor Set Amet Adipiscing</h2>
  <p class="abs">Lorem ipsum dolor sit amet, consectetur adipiscing elit, sed do eiusmod tempor incididunt ut labore et dolore magna aliqua. Ut enim ad minim veniam, quis nostrud exercitation ullamco laboris enim ad minim veniam, quis exercitation ullamco.</p>
  <div class="btn btn-green" style="left:453px;top:375px;width:176px">Sign up</div>
</section>

<h2 class="abs news-title">News and Updates</h2>
<p class="abs news-sub">Lorem ipsum dolor sit amet, consectetur adipiscing elit</p>
<article class="news" style="left:133px">
  <div class="thumb" role="img" aria-label="City skyline with a bridge at dusk" style="background:linear-gradient(180deg,#6a4f86 0%,#c06a8a 55%,#2f3a5c 100%)"></div>
  <div class="date">01<small>JAN</small></div>
  <h3>Lorem ipsum dolor</h3>
  <p>Lorem ipsum dolor sit amet, con sectet ncing elit, sed do eiusm tempor incididunt ut labore et dolore magna aliqua. Sed ut per spiciatis unde omnis iste natus error sit voluptatem.</p>
  <a>Read more &gt;</a>
</article>
<article class="news" style="left:608px">
  <div class="thumb" role="img" aria-label="Person smiling while using a phone outdoors" style="background:linear-gradient(135deg,#cfd9d4 0%,#9fb3a8 60%,#d98a7a 100%)"></div>
  <div class="date">07<small>JAN</small></div>
  <h3>Lorem ipsum dolor</h3>
  <p>Lorem ipsum dolor sit amet, con sectet ncing elit, sed do eiusm tempor incididunt ut labore et dolore magna aliqua. Sed ut per spiciatis unde omnis iste natus error sit voluptatem.</p>
  <a>Read more &gt;</a>
</article>

<footer class="abs footer">
  <div class="brand"><span class="brand-dot"></span>Marrowind</div>
  <p class="about">Lorem ipsum dolor sit amet, consectetur adipiscing elit, sed do eiusmod tempor incididunt ut labore</p>
  <div class="socials"><span></span><span></span><span></span><span></span></div>

  <div class="contact" style="top:62px"><svg width="14" height="18" aria-hidden="true"><path d="M7 1 C3 1 1 4 1 7 C1 11 7 17 7 17 C7 17 13 11 13 7 C13 4 11 1 7 1 Z" fill="var(--green)"/><circle cx="7" cy="7" r="2.5" fill="#fff"/></svg><span>Unit 4, Larkfield Court, Brambly,<br>KL7 2RT</span></div>
  <div class="contact" style="top:132px"><svg width="16" height="12" aria-hidden="true"><rect x="1" y="1" width="14" height="10" fill="none" stroke="var(--green)" stroke-width="1.5"/><path d="M1 1 L8 7 L15 1" fill="none" stroke="var(--green)" stroke-width="1.5"/></svg><span>hello@marrowind.net</span></div>
  <div class="contact" style="top:188px"><svg width="14" height="14" aria-hidden="true"><path d="M2 1 L5 1 L6 5 L4 6 C5 8 6 9 8 10 L9 8 L13 9 L13 12 C7 13 1 7 2 1 Z" fill="var(--green)"/></svg><span>+1(55)010 - 284 - 3961</span></div>

  <div class="field" style="left:688px;top:60px;width:182px">Your Name</div>
  <div class="field" style="left:885px;top:60px;width:182px">Your Email</div>
  <div class="field" style="left:688px;top:104px;width:379px">Subject</div>
  <div class="field" style="left:688px;top:148px;width:379px;height:80px">Message</div>
  <div class="btn btn-green" style="left:790px;top:245px;width:176px;height:26px">Submit</div>
</footer>

<div class="abs bottom-bar">
  <span class="copy">©2018 All Rights Reserved</span>
  <nav><span>Home</span><span>How it works</span><span>About</span><span>Interior</span><span>Contact us</span></nav>
</div>

</body>
</html>
```